Banner Design needed for Campus Recruitment Purpose!

Both Vortek5 and Harlow Quest & Associates is partner firms while Vortek5 is a career and talent management specialist, Harlow Quest & Associates focused on providing a premium executive search and recruitment services.

Banner designs are meant for our upcoming campus career fair exhibition and we requires a total of 3 banner designs that gives off a professional and mature vibes.
• 2 vertical banners design (approximately 61cm by 198cm)
• 1 expandable exhibition display banner design as the backdrop of our booth (approximately 230 cm by 230cm)
P.S. I have uploaded a sample of how the expandable exhibition display stand is like so you can have an idea of how big it is.

Purpose of exhibition is to:
• Introduce and recruit associates for Harlow Quest & Associates
• Introduce and promote PeakStride, a career consulting program under Vortek5, to individuals with the aim of imparting knowledge to enhance their ability and chances to get a job!

1. First Vertical Banner Design for Harlow Quest & Associates has to include:
• Harlow Quest & Associates Logo
• Harlow Quest & Associates Slogan: The preferred firm for premium executive search and recruitment services globally
• Relevant graphics relating to executive search services
• 5 bullet points of our services which is,
o Executive Search & Recruitment
o Contract Placement
o Onboarding Coaching
o Executive Coaching
o Leadership Assessment
• Background color of the banner has to be the same as the logo’s background which is the charcoal grey
• Color theme used in the banner has to match the Harlow’s logo colors

2. Second Vertical Banner Design for Vortek5’s PeakStride has to include:
• Vortek5’s Logo
• Vortek5’s Slogan: Career & Talent Management Specialists
• Relevant graphics
• Suitable wording design for the word, “PeakStride”
• Do create an area to include brief information of the program

3. Design for expandable exhibition display banner has to include:
• Logos of both Vortek5 and Harlow Quest & Associates
• Right side: Vortek5, Left side: Harlow Quest & Associates
• Require your help to blend and design the background whereby it can complement both logos with aim of making them into one picture

Target Market(s)

Individuals of age 25 - 40

Industry/Entity Type

Management

Font styles to use
Serif
Sans Serif

Requirements
Should not have
• The banners should not look too casual or playful.

```html
<!DOCTYPE html>
<html lang="en">
<head>
<meta charset="utf-8">
<title>Harlow Quest &amp; Associates — Vertical Banner</title>
<link href="https://fonts.googleapis.com/css2?family=Libre+Baskerville&display=swap" rel="stylesheet">
<style>
  :root {
    --charcoal: #1b1b1b;
    --charcoal-deep: #141414;
    --olive: #8b8849;
    --gold: #a0975a;
    --white: #ffffff;
    --photo-dark: #3a3d44;
    --photo-light: #b9c1c9;
  }
  * { margin: 0; padding: 0; box-sizing: border-box; }
  html, body { width: 1200px; height: 3888px; overflow: hidden; background: var(--charcoal); }
  .banner {
    position: relative;
    width: 1200px;
    height: 3888px;
    background: linear-gradient(180deg, var(--charcoal-deep) 0%, var(--charcoal) 40%, var(--charcoal) 100%);
    font-family: "Libre Baskerville", "Times New Roman", serif;
    color: var(--white);
    overflow: hidden;
  }
  .shapes { position: absolute; inset: 0; }
  .brand {
    position: absolute;
    top: 250px;
    left: 200px;
    display: flex;
    align-items: center;
    gap: 40px;
    color: var(--gold);
  }
  .brand-mark { width: 110px; height: 110px; border-radius: 50%; background: var(--gold); flex: none; }
  .brand-name { line-height: 1.1; }
  .brand-name .line-main { display: block; font-size: 92px; letter-spacing: 4px; }
  .brand-name .line-sub { display: block; font-size: 46px; letter-spacing: 6px; margin-top: 10px; }
  .slogan {
    position: absolute;
    top: 880px;
    left: 0;
    width: 1200px;
    text-align: center;
    text-transform: uppercase;
    line-height: 1.08;
  }
  .slogan .small { display: block; font-size: 72px; }
  .slogan .large { display: block; font-size: 128px; }
  .slogan .medium { display: block; font-size: 92px; }
  .services {
    position: absolute;
    top: 2720px;
    left: 0;
    width: 1200px;
    list-style: none;
    text-align: center;
    text-transform: uppercase;
  }
  .services li {
    font-size: 52px;
    line-height: 1.45;
    width: 600px;
    margin: 0 auto;
    padding: 26px 0;
    border-bottom: 4px solid var(--olive);
  }
  .services li:first-child { padding-top: 0; }
  .services li:last-child { border-bottom: none; }
</style>
</head>
<body>
<main class="banner">
  <svg class="shapes" width="1200" height="3888" viewBox="0 0 1200 3888" aria-hidden="false">
    <defs>
      <linearGradient id="officeTones" x1="0" y1="0" x2="1" y2="0">
        <stop offset="0" stop-color="var(--photo-dark)"/>
        <stop offset="0.45" stop-color="#5b6068"/>
        <stop offset="1" stop-color="var(--photo-light)"/>
      </linearGradient>
    </defs>
    <polygon class="slogan-band" points="0,980 1200,560 1200,1690 0,1990" fill="var(--olive)"/>
    <polygon class="office-photo" role="img" aria-label="Executive in a suit reading documents at a desk by a high-rise office window"
             points="0,1990 1200,1690 1200,2290 0,2560" fill="url(#officeTones)"/>
    <polygon class="accent-stripe" points="0,2560 1200,2290 1200,2360 0,2640" fill="var(--olive)"/>
  </svg>

  <header class="brand">
    <span class="brand-mark"></span>
    <span class="brand-name">
      <span class="line-main">HARLOW QUEST</span>
      <span class="line-sub">&amp; ASSOCIATES</span>
    </span>
  </header>

  <h1 class="slogan">
    <span class="small">The Preferred</span>
    <span class="large">Firm For</span>
    <span class="large">Premium</span>
    <span class="small">Executive Search and</span>
    <span class="medium">Recruitment</span>
    <span class="small">Services Globally</span>
  </h1>

  <ul class="services">
    <li>Executive Search &amp;<br>Recruitment</li>
    <li>Contract<br>Placement</li>
    <li>Onboarding<br>Coaching</li>
    <li>Executive<br>Coaching</li>
    <li>Leadership<br>Assessment</li>
  </ul>
</main>
</body>
</html>
```